Stem Cell Facial

B0 Paper Size Poster for the Window. We are a high end Beauty Salon / Day Spa in Sydney NSW Australia.
Must be Organic looking but also attract attention. Must be modern, contemporary, clean and bold. Must our Salon Logo (velunara) (attached). The other image attached can be used, but are more of an indication of the desired look and feel. The word doc contains words that must to be used. Image of female face experiencing a beauty treatment could be used.
The Poster should be in Portrait (not Landscape)
Beauty Salon

```html
<!DOCTYPE html>
<html lang="en">
<head>
<meta charset="utf-8">
<title>Stem Cell Facial – velunara salon &amp; spa</title>
<link rel="stylesheet" href="https://fonts.googleapis.com/css2?family=Cabin:wght@400;600;700&family=Lato:wght@300;400;700;900&display=swap">
<style>
  :root {
    --leaf: #9dc93b;
    --leaf-dark: #7fa82a;
    --charcoal: #3a393b;
    --ink: #1b1b1c;
    --berry: #c0170f;
    --berry-dark: #8e0f09;
    --paper: #ffffff;
    --photo-light: #eef0f3;
    --photo-skin: #e8cfc2;
    --photo-hair: #1c1a1c;
  }
  * { margin: 0; padding: 0; box-sizing: border-box; }
  html, body { width: 1169px; height: 1200px; overflow: hidden; background: var(--paper); }
  .poster {
    position: absolute; left: 0; top: 0;
    width: 1366px; height: 1402px;
    transform: scale(0.8558); transform-origin: 0 0;
    font-family: "Cabin", "Lato", sans-serif;
    color: var(--paper);
  }
  .shapes { position: absolute; inset: 0; }
  .abs { position: absolute; }

  .banner-text { left: 40px; width: 273px; text-align: center; }
  .banner-title { top: 62px; font-family: "Lato", sans-serif; font-weight: 300; font-size: 35px; line-height: 43px; letter-spacing: 0.5px; }
  .dots { left: 55px; width: 243px; border-top: 3px dotted var(--paper); }
  .dots--upper { top: 230px; }
  .dots--lower { top: 440px; }
  .banner-offer { top: 268px; font-weight: 700; font-size: 62px; line-height: 70px; }
  .banner-tagline { top: 482px; font-family: "Lato", sans-serif; font-weight: 300; font-size: 29px; line-height: 36px; }
  .banner-tagline strong { font-family: "Cabin", sans-serif; font-weight: 700; }

  .callout { left: 160px; top: 730px; width: 290px; font-weight: 700; font-size: 44px; line-height: 54px; }
  .callout .big { font-size: 64px; }
  .price { font-family: "Cabin", sans-serif; font-weight: 700; line-height: 1; }
  .price sup { font-size: 0.42em; vertical-align: 0.95em; margin-left: 2px; }
  .price--facials { left: 106px; top: 906px; font-size: 96px; }
  .save { left: 108px; top: 1036px; width: 342px; text-align: center; font-weight: 700; font-size: 40px; }

  .creme-label { left: 498px; top: 1040px; width: 300px; text-align: center; font-weight: 700; font-size: 33px; }
  .price--creme { left: 522px; top: 1100px; font-size: 86px; }
  .bonus { left: 498px; top: 1206px; width: 300px; text-align: center; font-weight: 700; font-size: 38px; }

  .disclaimer {
    left: 56px; top: 1362px; transform: rotate(-90deg); transform-origin: 0 0;
    font-family: Arial, "Lato", sans-serif; font-size: 37px; white-space: nowrap;
  }

  .brand { left: 962px; top: 1200px; width: 352px; }
  .brand-name { font-family: "Cabin", sans-serif; font-weight: 700; font-size: 78px; line-height: 86px; color: var(--leaf); text-align: center; letter-spacing: -1px; }
  .brand-rule { border-top: 2px solid #cfcfcf; margin-top: 2px; }
  .brand-sub { font-family: "Lato", sans-serif; font-weight: 700; font-size: 25px; letter-spacing: 16.5px; margin-top: 6px; white-space: nowrap; }
  .brand-phone { display: flex; align-items: center; gap: 14px; margin-top: 12px; font-family: "Lato", sans-serif; font-weight: 700; font-size: 34px; letter-spacing: 17px; white-space: nowrap; }
</style>
</head>
<body>
<main class="poster">
  <svg class="shapes" viewBox="0 0 1366 1402" width="1366" height="1402">
    <defs>
      <linearGradient id="photo-tone" x1="0" y1="0" x2="1" y2="1">
        <stop offset="0" stop-color="var(--photo-hair)"/>
        <stop offset="0.35" stop-color="#5a4a48"/>
        <stop offset="0.55" stop-color="var(--photo-skin)"/>
        <stop offset="1" stop-color="var(--photo-light)"/>
      </linearGradient>
    </defs>
    <rect class="backdrop" x="25" y="20" width="1316" height="1356" fill="var(--charcoal)"/>
    <path class="curve-band" d="M315 20 C 350 620, 780 1130, 1341 1212 L1341 20 Z" fill="var(--paper)"/>
    <path class="hero-photo" role="img" aria-label="Photo of a young woman with short dark hair resting her face on her hands, showing smooth glowing skin"
          d="M345 20 C 385 600, 810 1100, 1341 1185 L1341 20 Z" fill="url(#photo-tone)"/>

    <polygon class="ribbon-banner" points="40,22 313,22 313,700 176,628 40,700" fill="var(--leaf)"/>

    <!-- facials tag -->
    <polygon class="tag-tail" points="240,1100 355,1100 290,1160 240,1160" fill="var(--berry)"/>
    <polygon class="tag-fold" points="240,1160 290,1160 290,1196" fill="var(--leaf-dark)"/>
    <rect class="tag-body" x="108" y="760" width="342" height="342" rx="18" fill="var(--leaf)"/>
    <polygon class="callout-box" points="160,722 438,722 450,734 450,930 415,870 160,870 146,856 146,736" fill="var(--ink)"/>
    <polygon class="price-band" points="90,905 468,905 468,1015 455,1028 455,1015 90,1015" fill="var(--berry)"/>

    <!-- creme tag -->
    <polygon class="tag-tail" points="610,1265 720,1265 612,1352" fill="var(--berry)"/>
    <rect class="tag-body" x="498" y="1020" width="300" height="248" rx="18" fill="var(--leaf)"/>
    <polygon class="price-band" points="483,1097 815,1097 815,1190 800,1200 800,1190 483,1190" fill="var(--berry)"/>
  </svg>

  <div class="abs banner-text banner-title">ANTI AGEING<br>FACIAL<br>REJUVENATION</div>
  <div class="abs dots dots--upper"></div>
  <div class="abs banner-text banner-offer">SPECIAL<br>OFFER!!</div>
  <div class="abs dots dots--lower"></div>
  <div class="abs banner-text banner-tagline">EXPERIENCE THE<br><strong>POWER OF PLANT</strong><br>STEM CELLS</div>

  <div class="abs callout"><span class="big">2</span> STEM CELL<br>FACIALS FOR</div>
  <div class="abs price price--facials">$249.<sup>99</sup></div>
  <div class="abs save">SAVE OVER $50</div>

  <div class="abs creme-label">STEM CELL CRÈME</div>
  <div class="abs price price--creme">$89.<sup>95*</sup></div>
  <div class="abs bonus">BONUS FREE</div>

  <div class="abs disclaimer">*while stocks last</div>

  <div class="abs brand">
    <div class="brand-name">velunara</div>
    <div class="brand-rule"></div>
    <div class="brand-sub">salon &amp; spa</div>
    <div class="brand-phone">
      <svg width="26" height="28" viewBox="0 0 26 28" aria-hidden="true">
        <rect x="1" y="1" width="24" height="26" rx="5" fill="var(--paper)"/>
        <path d="M9 6 L12 6 L13 10 L11 12 Q13 16 15 17 L17 15 L20 16 L20 20 Q14 22 9 14 Q7 10 9 6 Z" fill="var(--charcoal)"/>
      </svg>
      <span>9381 5067</span>
    </div>
  </div>
</main>
</body>
</html>
```